Lumvask Project

We need a simple corporate website with 3-4 pages total.
We already have the logo and text.
We like the scroll design
we like this look, feel and design http://norvelpix.com

Target Market(s)

The target market is B to B and consumer brands and vendors/distributors

Font styles to use
Serif

Colors
eaf1f7
f5f5f5
ffffff

Requirements
Must have
• Must be a coded website and put in place with wordpress
we like the scroll design

```html
<!DOCTYPE html>
<html lang="en">
<head>
<meta charset="utf-8">
<title>Lumvask</title>
<link href="https://fonts.googleapis.com/css2?family=Signika:wght@300;400;600&family=PT+Sans:wght@400;700&display=swap" rel="stylesheet">
<style>
:root{
  --brown:#5b2e12;
  --blue:#1e98d4;
  --blue-dark:#1577b0;
  --text:#6a6a6a;
  --nav:#555;
  --band:#efefef;
  --white:#ffffff;
  --footer:#1f1f1f;
  --footer-text:#e6e6e6;
  --frame:#ffffff;
}
*{margin:0;padding:0;box-sizing:border-box}
html,body{width:1200px;height:2192px;overflow:hidden}
body{position:relative;background:var(--white);font-family:"PT Sans",sans-serif;color:var(--text)}
.abs{position:absolute}

/* header */
.site-header{position:absolute;left:0;top:0;width:1200px;height:134px;background:var(--white)}
.brand{position:absolute;left:139px;top:22px;width:110px;text-align:center}
.brand-mark{display:block;width:62px;height:52px;margin:0 auto 6px;background:var(--blue);border-radius:6px}
.brand-name{font-family:"Signika",sans-serif;font-weight:600;font-size:27px;letter-spacing:1px;color:var(--brown);line-height:1}
.search{position:absolute;left:849px;top:26px;width:221px;height:34px;border:1px solid #dcdcdc;border-radius:3px;background:#f7f7f7;font-size:11px;color:#aaa;padding:10px 0 0 14px}
.search svg{position:absolute;right:10px;top:7px}
.main-nav{position:absolute;right:130px;top:98px;display:flex;font-family:"Signika",sans-serif;font-size:13px;color:var(--nav)}
.main-nav span{padding:0 14px}
.main-nav .sep{padding:0;color:#777}
.main-nav .current{color:var(--blue)}

/* hero */
.hero{position:absolute;left:0;top:134px;width:1200px;height:591px;background:linear-gradient(100deg,#e8e4df 0%,#f3efe9 30%,#d9cbbd 55%,#efe9e2 80%,#cfc7bf 100%)}
.slide-arrow{position:absolute;top:412px;width:40px;height:40px}
.slide-arrow.prev{left:78px}
.slide-arrow.next{left:1082px}

/* about */
.section-title{font-family:"Signika",sans-serif;font-weight:400;color:var(--brown);font-size:29px}
.about-title{position:absolute;left:132px;top:778px}
.about-photo{position:absolute;left:130px;top:843px;width:298px;height:167px;border:4px solid var(--frame);box-shadow:0 0 2px rgba(0,0,0,.25);background:linear-gradient(120deg,#c9c3bb,#6e5a4a 45%,#9c8a78 75%,#d7d2cc)}
.about-text{position:absolute;font-size:12.6px;line-height:20.4px;color:var(--text)}
.about-text.lead{left:455px;top:840px;width:615px}
.about-text.more{left:132px;top:1035px;width:940px}

/* services */
.services{position:absolute;left:0;top:1153px;width:1200px;height:608px;background:var(--band)}
.services-title{position:absolute;left:0;top:30px;width:1200px;text-align:center}
.services-arrows{position:absolute;left:1020px;top:48px}
.service{position:absolute;width:348px;text-align:center}
.service-photo{width:348px;height:152px;border:3px solid var(--frame);box-shadow:0 0 2px rgba(0,0,0,.2)}
.service-name{font-family:"Signika",sans-serif;font-size:26px;color:var(--blue);margin-top:20px}

/* team */
.team-grid{position:absolute}
.team-photo{position:absolute;width:79px;height:80px}
.team-title{position:absolute;left:681px;top:1822px}
.team-text{position:absolute;left:681px;top:1874px;width:384px;font-size:12.6px;line-height:20.8px;color:var(--text)}

/* footer */
.site-footer{position:absolute;left:0;top:2067px;width:1200px;height:125px;background:var(--footer);color:var(--footer-text)}
.footer-nav{position:absolute;left:132px;top:32px;display:flex;font-size:13px}
.footer-nav span{padding:0 12px}
.footer-nav span:first-child{padding-left:0}
.copyright{position:absolute;left:132px;top:72px;font-size:12.5px}
.copyright b{font-weight:400;color:var(--blue)}
.social{position:absolute;left:878px;top:32px;display:flex;gap:10px}
.social span{display:block;width:40px;height:40px;border-radius:6px}
</style>
</head>
<body>

<header class="site-header">
  <div class="brand">
    <span class="brand-mark"></span>
    <div class="brand-name">LUMVASK</div>
  </div>
  <div class="search">Search...
    <svg width="20" height="20" viewBox="0 0 20 20"><circle cx="8" cy="8" r="5.5" fill="none" stroke="#333" stroke-width="2"/><line x1="12" y1="12" x2="18" y2="17" stroke="#333" stroke-width="3" stroke-linecap="round"/></svg>
  </div>
  <nav class="main-nav">
    <span class="current">Home</span><span class="sep">|</span>
    <span>About</span><span class="sep">|</span>
    <span>Services</span><span class="sep">|</span>
    <span>Our Team</span><span class="sep">|</span>
    <span>Projects</span><span class="sep">|</span>
    <span style="padding-right:0">Contact</span>
  </nav>
</header>

<section class="hero" role="img" aria-label="Smiling woman lying on a rug with a laptop and credit card, shopping bags beside her"></section>
<svg class="slide-arrow prev" viewBox="0 0 40 40"><circle cx="20" cy="20" r="19" fill="var(--blue)" stroke="#fff" stroke-width="2"/><path d="M23 12 L14 20 L23 28 Z" fill="#fff"/></svg>
<svg class="slide-arrow next" viewBox="0 0 40 40"><circle cx="20" cy="20" r="19" fill="var(--blue)" stroke="#fff" stroke-width="2"/><path d="M17 12 L26 20 L17 28 Z" fill="#fff"/></svg>

<h2 class="section-title about-title">About Lumvask</h2>
<div class="about-photo" role="img" aria-label="Hand holding a tablet showing an online store next to a card"></div>
<p class="about-text lead">Lumvask Interactive group is primarily focused on digital commerce operating businesses. Currently, the Lumvask Interactive group consists of Lumvask Interactive Corporation’s subsidiaries Fieldrun.com, KRVshop.com, PennyHound.com, StrideSaver.com and CycleCommons.com (note to web designer more E-commerce platforms to be added this year) (baby care)(pet supplies), (luxury beauty) All easy-to-navigate sites are linked together by the promise to make life a little easier with fast, free shipping on orders over $35, award-winning 24/7 customer care and one shared cart and checkout. Lumvask Interactive continues to redefine e-commerce by changing the way people shop for almost every part of their lives. At Lumvask Interactive we dare to think big and explore possibilities.</p>
<p class="about-text more">Lumvask Interactive flagship store is DepotLaneDirect.com , a central destination where consumers can find everything consumer goods. Lumvask Interactive is one of those special places where people love coming to work every day. We work hard, play hard, and we’re on a mission to bring real variety and value to online shopping. Our workplace is a positive, energized and respectful atmosphere, where people and their ideas are highly valued.</p>

<section class="services">
  <h2 class="section-title services-title">Lumvask Services</h2>
  <svg class="services-arrows" width="36" height="22" viewBox="0 0 36 22"><path d="M13 3 L5 11 L13 19" fill="none" stroke="#333" stroke-width="4"/><path d="M23 3 L31 11 L23 19" fill="none" stroke="#333" stroke-width="4"/></svg>

  <div class="service" style="left:194px;top:116px">
    <div class="service-photo" role="img" aria-label="Hands holding a card over a laptop keyboard" style="background:linear-gradient(135deg,#d8c8b8,#9a7a62 45%,#2f2f2f 85%)"></div>
    <div class="service-name">E-Commerce</div>
  </div>
  <div class="service" style="left:658px;top:116px">
    <div class="service-photo" role="img" aria-label="Woman shopping online beside a lit holiday tree" style="background:linear-gradient(90deg,#3d4a2a,#7b6a3a 40%,#b08a86 70%,#6e2a36)"></div>
    <div class="service-name">Online Retail</div>
  </div>
  <div class="service" style="left:194px;top:370px">
    <div class="service-photo" role="img" aria-label="Shop assistant and cashier at a store counter" style="background:linear-gradient(90deg,#8a5a3a,#7fa6d6 35%,#c9b8a8 65%,#7a3a34)"></div>
    <div class="service-name">Retail</div>
  </div>
  <div class="service" style="left:658px;top:370px">
    <div class="service-photo" role="img" aria-label="Keyboard with a red shopping cart key" style="background:radial-gradient(circle at 55% 50%,#c0262c 0 18%,#b9bcc0 22%,#9ea1a5 60%,#d6d8da)"></div>
    <div class="service-name">Shopping</div>
  </div>
</section>

<div class="team-grid" style="left:158px;top:1830px;width:480px;height:162px" role="img" aria-label="Grid of team member portraits">
  <div class="team-photo" style="left:0;top:0;background:#8aa07a"></div>
  <div class="team-photo" style="left:80px;top:0;background:#b59a86"></div>
  <div class="team-photo" style="left:160px;top:0;background:#9a7a66"></div>
  <div class="team-photo" style="left:240px;top:0;background:#c9b68a"></div>
  <div class="team-photo" style="left:320px;top:0;background:#8c8a78"></div>
  <div class="team-photo" style="left:400px;top:0;background:#a89c8e"></div>
  <div class="team-photo" style="left:38px;top:81px;background:#b8ac98"></div>
  <div class="team-photo" style="left:118px;top:81px;background:#8a6a56"></div>
  <div class="team-photo" style="left:198px;top:81px;background:#a07a6a"></div>
  <div class="team-photo" style="left:278px;top:81px;background:#4a4a4e"></div>
  <div class="team-photo" style="left:358px;top:81px;background:#8a9a7a"></div>
</div>
<h2 class="section-title team-title">Our Team</h2>
<p class="team-text">Sed ut perspiciatis unde omnis iste natus error sit voluptatem accusantium doloremque laudantium, totam rem aperiam, eaque ipsa quae ab illo inventore veritatis et quasi architecto beatae vitae dicta sunt explicabo. Nemo enim ipsam voluptatem quia voluptas sit aspernatur aut odit aut fugit, sed quia consequuntur magni dolores eos qui ratione voluptatem sequi nesciunt.</p>

<footer class="site-footer">
  <nav class="footer-nav">
    <span>Home</span>|<span>About</span>|<span>Services</span>|<span>Our Team</span>|<span>Projects</span>|<span>Contact</span>
  </nav>
  <p class="copyright">©2013 <b>Lumvask</b>. All rights reserved.</p>
  <div class="social">
    <span style="background:#3b5ea6"></span>
    <span style="background:#3aa6d8"></span>
    <span style="background:#d8483a"></span>
    <span style="background:#c4302b"></span>
  </div>
</footer>

</body>
</html>
```